Cedar Hollow Growth Institute is changing lives and needs a state of the art PageLoom Business Web

We are looking for lots of WOW factor. We need a state of the art website that inspires people to take action toward changing their life. We have some award winning trademarked programs that we are looking to introduce through our website.

The Top Portion will have a place holder for a welcome video (currently being recorded) and this brief description of the business along side of it:
=====================================================
Let’s face it. Life is hard. Being human isn’t easy for any of us. Here, at the Cedar Hollow Growth Institute, we understand that simple truth. We know that having a strong self-worth first requires you to be aware of your value as a Human Being. Human potential is the HIGHEST value that creation has to offer.

Regardless of whether you see it through the eyes of evolution or through the eyes of religion, the truth of the matter is that Human Beings are of significant value. Abundance is our birthright! Our focus is on developing that human potential.

There is only one thing holding you back from experiencing overflowing abundance – YOU! Ask yourself, why haven’t I experienced that true transformation, in my life, that attracts abundance?

What if there was a way to remove the uncertainty tied to the labyrinth of life? What if you no longer have to be a victim of the unpredictable? Well, the good news is – Its Possible! There is an amazing amount of potential locked away deep inside you. Potential that has the capacity to release you from your current patterns of thinking and launch a complete turning point in your life.

The Cedar Hollow Growth Institute recognizes this potential, often before you recognize it in yourself, and is excited to partner with you on your journey to becoming an unstoppable force. We look forward to resourcing you with the tools and training that will help you synchronize your desire and your direction with your destiny!
============================================================

Under the welcome / intro block, we would like to have a gallery that scrolls through pictures, and inspirational quotes. We can also use this to advertise
our services and special deals on programs.

Next section can outline our lanes of business or focus areas:

High Performance Living
Business Coaching & Consultancy
Digital Resources Center

Here is the template we would like to leverage: https://pageloom-sites.example/theme/harvestline
or you can be creative and provide one you think would work best....

Should have some awesome photos, descriptions, etc....

Here are some samples to model after:

https://vantorix.example/
https://www.kelvo-mentoring.example/
http://dorianwexley.example/

https://brennocorteam.example/talk/?c=brc-se-bo&brtc=brt-core&gclid=QzLmPfRtYvWxNcBaKjHgDsEuIoPaLkMnBvCxZqWeRtYuIoPaSdFgHjKlZxCvBnMqWeRtYuIoPaSdFg

https://laurent-okafor.example/
https://www.mymindforge.example/
https://www.tobiasfenwick.example/

Target Market(s)

Business Leaderships and anyone interested in personal development and growth

Industry/Entity Type

Leadership

Coding

Coded - Design and coding required

Font styles to use
Serif
Sans Serif
Decorative
Script

Colors

Designer to choose colors to be used in the design.

Requirements
Must have
• Business Name, Logo, and brief introduction paragraph. Must have space for the welcome video.
• We do not have any current site but do already own the domain for it:
• https://chgrow.example/ is the PageLoom site we will be using once we choice a winner to work with
• Must use our Taglines:
• Shaping the existence of individuals, organizations, and communities...
• Make your life the grandest parade in town!
• =====================================================
• Would like music to softly play in back ground when people land on the page. This song could repeat in the background: https://www.vidstreamo.example/watch?v=QxTr7vLmNaP&list=ZKw3HtYbRcUoFgEiMnJsLpQaVdXzCyBt92&index=4
• You can also cycle through the entire soundtrack of the RINGMASTER'S DREAM - all those songs work perfectly with our themes
• You must also blend the content available on this site with the new site:
• https://www.brennocorgroup.example/dwaynehollister
Nice to have
• would like music to softly play in back ground when people land on the page. This song could repeat in the softly in the background: https://www.vidstreamo.example/watch?v=QxTr7vLmNaP&list=ZKw3HtYbRcUoFgEiMnJsLpQaVdXzCyBt92&index=4
Should not have
• Ads, empty white space, negative perspectives, etc....

```html
<!DOCTYPE html>
<html lang="en">
<head>
<meta charset="UTF-8">
<title>Cedar Hollow Growth Institute</title>
<link rel="stylesheet" href="https://fonts.googleapis.com/css2?family=Cinzel:wght@400;700&family=Open+Sans:ital,wght@0,400;0,600;1,400&display=swap">
<style>
:root{
  --navy:#1f2270;
  --royal:#2a3190;
  --deep:#1a1c5c;
  --white:#ffffff;
  --ink:#2b2b2b;
  --mist:#e9e9eb;
  --footer:#2f2e31;
  --footer-base:#232225;
  --footer-text:#cfcfd2;
}
*{margin:0;padding:0;box-sizing:border-box}
html,body{width:1200px;height:2927px;overflow:hidden}
body{font-family:"Open Sans",Arial,sans-serif;color:var(--ink);position:relative;background:var(--white)}

/* Hero */
.hero{position:absolute;left:0;top:0;width:1200px;height:760px;overflow:hidden}
.hero-photo{position:absolute;inset:0;background:
  radial-gradient(ellipse 420px 220px at 620px 540px,#7fa3b4 0%,#3d5f72 35%,rgba(20,32,44,0) 75%),
  linear-gradient(180deg,#0f1820 0%,#22394a 45%,#1a2d3a 65%,#05090d 100%)}
.nav a{position:absolute;color:var(--white);text-decoration:none;font-family:"Cinzel",Georgia,serif;font-size:16px;font-weight:700;letter-spacing:.5px;white-space:nowrap}
.nav .left{top:68px}
.nav .right{top:61px}
.brand{position:absolute;left:480px;top:20px;width:240px;text-align:center;color:var(--white)}
.brand-mark{display:block;width:44px;height:44px;border-radius:50%;border:2px solid var(--white);margin:0 auto 8px}
.brand-name{font-family:"Cinzel",Georgia,serif;font-size:22px;font-weight:400;line-height:24px;white-space:nowrap}
.play{position:absolute;left:562px;top:246px;width:76px;height:76px}
.tagline{position:absolute;top:336px;left:0;width:1200px;text-align:center;color:var(--white);font-family:"Cinzel",Georgia,serif;font-weight:700;font-size:31px;line-height:39px;text-shadow:0 2px 6px rgba(0,0,0,.5)}
.hero-curve{position:absolute;left:0;bottom:0;width:1200px;height:90px}

/* Welcome */
.welcome{position:absolute;left:0;top:760px;width:1200px;height:665px;background:linear-gradient(180deg,#ffffff 0%,#f2f2f3 55%,var(--mist) 100%);text-align:center}
.welcome-mark{display:block;width:76px;height:76px;border-radius:50%;background:var(--navy);margin:0 auto}
.welcome h1{font-family:"Cinzel",Georgia,serif;color:var(--navy);font-size:33px;font-weight:700;margin-top:6px;letter-spacing:.5px}
.welcome-copy{width:980px;margin:28px auto 0;font-size:15.5px;line-height:27px;color:var(--ink)}
.welcome-copy p+p{margin-top:27px}

/* Gallery */
.gallery{position:absolute;left:0;top:1425px;width:1200px;height:530px;background:var(--royal)}
.gallery-notch{position:absolute;left:530px;top:-2px;width:140px;height:40px}
.gallery h2,.focus h2{font-family:"Cinzel",Georgia,serif;color:var(--white);font-size:31px;font-weight:700;text-align:center;letter-spacing:.5px}
.gallery h2{margin-top:48px}
.slide{position:absolute;top:120px;width:480px;height:314px;overflow:hidden}
.slide-photo{position:absolute;inset:0}
.slide-one .slide-photo{background:linear-gradient(180deg,#3f8a8c 0%,#2a5d63 45%,#0c1416 100%)}
.slide-two .slide-photo{background:radial-gradient(ellipse 220px 160px at 290px 150px,#b88a4f 0%,#6a5a4c 50%,#3c3b40 100%)}
.slide-text{position:absolute;left:40px;right:40px;top:160px;text-align:center;color:var(--white);text-shadow:0 1px 4px rgba(0,0,0,.6)}
.slide-quote{font-style:italic;font-size:18px;line-height:29px}
.slide-author{font-weight:600;font-size:18px;margin-top:2px}
.arrow{position:absolute;top:248px;width:34px;height:60px}
.gallery-curve{position:absolute;left:0;bottom:-1px;width:1200px;height:70px}

/* Focus */
.focus{position:absolute;left:0;top:1955px;width:1200px;height:562px;overflow:hidden}
.focus-photo{position:absolute;inset:-70px 0 0 0;background:radial-gradient(ellipse 300px 300px at 880px 200px,#2e3aa2 0%,rgba(40,48,140,0) 70%),linear-gradient(180deg,#232a86 0%,var(--deep) 100%)}
.focus h2{position:relative;margin-top:52px}
.area{position:absolute;top:160px;width:260px;text-align:center;color:var(--white)}
.area-mark{display:block;width:80px;height:80px;border-radius:50%;border:3px solid var(--white);margin:0 auto}
.area h3{font-family:"Cinzel",Georgia,serif;font-size:21px;font-weight:700;line-height:28px;margin-top:22px}
.area p{font-size:13.5px;line-height:23px;margin-top:8px}
.read-more{display:inline-block;margin-top:24px;width:135px;height:46px;line-height:42px;border:2px solid var(--white);border-radius:23px;color:var(--white);text-decoration:none;font-size:14px;font-weight:600}

/* Footer */
.footer{position:absolute;left:0;top:2517px;width:1200px;height:332px;background:var(--footer);color:var(--footer-text)}
.footer-brand{position:absolute;left:155px;top:70px;width:240px;text-align:center;color:var(--white)}
.footer-brand .brand-mark{width:40px;height:40px}
.footer-brand .brand-name{font-size:23px;line-height:26px}
.footer-col{position:absolute;top:68px}
.footer-col h4{font-family:"Cinzel",Georgia,serif;color:var(--white);font-size:19px;font-weight:700;margin-bottom:14px}
.footer-col a{display:block;color:var(--footer-text);text-decoration:none;font-size:15px;line-height:31px}
.social a{padding-left:24px;position:relative}
.social a::before{content:"";position:absolute;left:0;top:10px;width:12px;height:12px;background:var(--footer-text)}
.copyright{position:absolute;left:0;top:2849px;width:1200px;height:78px;background:var(--footer-base);color:var(--footer-text);font-size:14px;text-align:center;line-height:78px}
</style>
</head>
<body>

<header class="hero">
  <div class="hero-photo" role="img" aria-label="Silhouettes of people jumping joyfully against a sunset over the sea"></div>
  <nav class="nav">
    <a class="left" href="#" style="left:155px">About Us</a>
    <a class="left" href="#" style="left:272px">Services</a>
    <a class="left" href="#" style="left:383px">Why Us</a>
    <a class="right" href="#" style="left:737px">Blogs</a>
    <a class="right" href="#" style="left:827px">Testimonials</a>
    <a class="right" href="#" style="left:982px">Contact</a>
  </nav>
  <div class="brand">
    <span class="brand-mark"></span>
    <div class="brand-name">Cedar Hollow<br>Growth Institute</div>
  </div>
  <svg class="play" viewBox="0 0 76 76" aria-label="Play welcome video">
    <circle cx="38" cy="38" r="35" fill="none" stroke="#fff" stroke-width="4"/>
    <circle cx="38" cy="38" r="28" fill="#fff"/>
    <path d="M31 25 L52 38 L31 51 Z" fill="#111"/>
  </svg>
  <div class="tagline">Shaping the existence of individuals,<br>organizations, and communities...<br>Make your life the grandest parade in town</div>
  <svg class="hero-curve" viewBox="0 0 1200 90" preserveAspectRatio="none">
    <path d="M0 90 L0 60 Q600 -40 1200 60 L1200 90 Z" fill="#ffffff"/>
  </svg>
</header>

<section class="welcome">
  <span class="welcome-mark"></span>
  <h1>Welcome to Cedar Hollow</h1>
  <div class="welcome-copy">
    <p>Let’s face it. Life is hard. Being human isn’t easy for any of us. Here, at the Cedar Hollow Growth Institute, we understand that simple truth. We know that having a strong self-worth first requires you to be aware of your value as a Human Being. Human potential is the HIGHEST value that creation has to offer.</p>
    <p>Regardless of whether you see it through the eyes of evolution or through the eyes of religion, the truth of the matter is that Human Beings are of significant value. Abundance is our birthright! Our focus is on developing that human potential. There is only one thing holding you back from experiencing overflowing abundance – YOU! Ask yourself, why haven’t I experienced that true transformation, in my life, that attracts abundance? What if there was a way to remove the uncertainty tied to the labyrinth of life? What if you no longer have to be a victim of the unpredictable? Well, the good news is – Its Possible! There is an amazing amount of potential locked away deep inside you. Potential that has the capacity to release you from your current patterns of thinking and launch a complete turning point in your life.</p>
    <p>The Cedar Hollow Growth Institute recognizes this potential, often before you recognize it in yourself, and is excited to partner with you on your journey to becoming an unstoppable force. We look forward to resourcing you with the tools and training that will help you synchronize your desire and your direction with your destiny!</p>
  </div>
</section>

<section class="gallery">
  <svg class="gallery-notch" viewBox="0 0 140 40">
    <path d="M0 0 Q40 0 55 25 Q70 45 85 25 Q100 0 140 0 Z" fill="#e9e9eb"/>
    <circle cx="70" cy="6" r="16" fill="#2a3190"/>
  </svg>
  <h2>Our Gallery</h2>
  <svg class="arrow" style="left:48px" viewBox="0 0 34 60"><path d="M30 4 L4 30 L30 56" fill="none" stroke="#fff" stroke-width="3"/></svg>
  <article class="slide slide-one" style="left:107px">
    <div class="slide-photo" role="img" aria-label="Silhouettes of friends helping each other up a rocky hill"></div>
    <div class="slide-text">
      <p class="slide-quote">Pellentesque faucibus Ut accumsan ultricies elit Maecenas at justo id velit placerat molestie Donec dictum</p>
      <p class="slide-author">By Author Name</p>
    </div>
  </article>
  <article class="slide slide-two" style="left:607px">
    <div class="slide-photo" role="img" aria-label="Group celebrating with raised arms on a mountain top at sunrise"></div>
    <div class="slide-text">
      <p class="slide-quote">Vivamus porttitor neque at volutpat rutrum purus nisi eleifend libero a tempus libero lectus feugiat felis Morbi</p>
      <p class="slide-author">By Author Name</p>
    </div>
  </article>
  <svg class="arrow" style="left:1118px" viewBox="0 0 34 60"><path d="M4 4 L30 30 L4 56" fill="none" stroke="#fff" stroke-width="3"/></svg>
  <svg class="gallery-curve" viewBox="0 0 1200 70" preserveAspectRatio="none">
    <path d="M0 0 Q600 120 1200 0 L1200 70 L0 70 Z" fill="#232a86"/>
  </svg>
</section>

<section class="focus">
  <div class="focus-photo" role="img" aria-label="Climber reaching down to pull a partner up a cliff, tinted deep blue"></div>
  <h2>Focus Areas</h2>
  <div class="area" style="left:167px">
    <span class="area-mark"></span>
    <h3>High Performance<br>Living</h3>
    <p>Vivamus porttitor neque at volutpat rutrum purus nisi eleifend libero a tempus libero lectus feugiat</p>
    <a class="read-more" href="#">READ MORE</a>
  </div>
  <div class="area" style="left:475px">
    <span class="area-mark"></span>
    <h3>Business Coaching<br>&amp; Consultancy</h3>
    <p>Vivamus porttitor neque at volutpat rutrum purus nisi eleifend libero a tempus libero lectus feugiat</p>
    <a class="read-more" href="#">READ MORE</a>
  </div>
  <div class="area" style="left:777px">
    <span class="area-mark"></span>
    <h3>Digital<br>Resources Center</h3>
    <p>Vivamus porttitor neque at volutpat rutrum purus nisi eleifend libero a tempus libero lectus feugiat</p>
    <a class="read-more" href="#">READ MORE</a>
  </div>
</section>

<footer class="footer">
  <div class="footer-brand">
    <span class="brand-mark"></span>
    <div class="brand-name">Cedar Hollow<br>Growth Institute</div>
  </div>
  <div class="footer-col" style="left:447px">
    <h4>Quick Links</h4>
    <a href="#">Home</a><a href="#">About Us</a><a href="#">Why Us</a><a href="#">Our Services</a>
  </div>
  <div class="footer-col" style="left:655px">
    <h4>Resources</h4>
    <a href="#">Blogs</a><a href="#">Testimonials</a><a href="#">Gallery</a><a href="#">Contact Us</a>
  </div>
  <div class="footer-col social" style="left:898px">
    <h4>Follow Us</h4>
    <a href="#">Circlepost</a><a href="#">Chirpline</a><a href="#">Worknet</a><a href="#">Snapframe</a>
  </div>
</footer>
<div class="copyright">© 2019 Company Name &nbsp;All right reserved</div>

</body>
</html>
```